VELTA

I want make nice catalogs for explin the my company specialties in spare part and maintenance in truck and heavy industry (bulldozer-excavator-dumper-wheel loader)<br/>I have service ultra fast delivery (spare parts) 7days just in 15days<br/>24 hour on site intervention<br/><br/>my site web: http://veltaparts.example

Colors

Designer to choose colors to be used in the design.

```html
<!DOCTYPE html>
<html lang="ar">
<head>
<meta charset="utf-8">
<title>VELTA Catalogue</title>
<link href="https://fonts.googleapis.com/css2?family=Cairo:wght@400;600;700&family=Montserrat:wght@600;800&display=swap" rel="stylesheet">
<style>
  :root {
    --backdrop: #eeeeee;
    --paper: #ffffff;
    --brand-red: #c8202a;
    --ink: #2b2b2b;
    --muted: #777777;
    --sky-top: #2f7fd0;
    --sky-bottom: #bcd9f2;
    --earth: #b98a55;
    --machine: #e9b320;
    --sea: #3c8fb8;
  }
  * { margin: 0; padding: 0; box-sizing: border-box; }
  html, body { width: 800px; height: 1200px; overflow: hidden; }
  body { background: var(--backdrop); position: relative; font-family: "Cairo", sans-serif; }

  .page {
    position: absolute; left: 227px; width: 365px;
    background: var(--paper);
    box-shadow: 0 2px 8px rgba(0,0,0,0.12);
    overflow: hidden;
  }
  .cover { top: 75px; height: 517px; }
  .back { top: 619px; height: 528px; }

  .brand { position: absolute; left: 18px; top: 30px; display: flex; align-items: center; gap: 8px; }
  .brand-square { width: 24px; height: 24px; background: var(--brand-red); }
  .brand-name { font-family: "Montserrat", sans-serif; font-weight: 800; font-size: 26px; color: var(--brand-red); letter-spacing: 1px; }
  .header-rule { position: absolute; left: 0; top: 92px; width: 245px; height: 3px; background: var(--brand-red); }

  .cover-photo {
    position: absolute; left: 0; top: 112px; width: 100%; height: 240px;
    background: linear-gradient(180deg, #9cc9e6 0%, var(--sea) 38%, #d9b27a 60%, var(--earth) 100%);
  }
  .focus-frame { position: absolute; left: 253px; top: 298px; width: 72px; height: 62px; border: 2px solid var(--brand-red); }

  .cover-title { position: absolute; right: 40px; top: 372px; text-align: right; line-height: 1.1; }
  .cover-title .line-1 { font-size: 42px; font-weight: 600; color: var(--ink); }
  .cover-title .line-2 { font-size: 42px; font-weight: 600; color: var(--brand-red); }

  .cover-sub { position: absolute; left: 85px; top: 470px; text-align: right; font-size: 11px; line-height: 1.45; color: var(--muted); width: 115px; }
  .cover-url { position: absolute; left: 213px; top: 484px; font-family: "Montserrat", sans-serif; font-weight: 600; font-size: 10px; color: var(--muted); }

  .back-photo {
    position: absolute; inset: 0;
    background: linear-gradient(180deg, var(--sky-top) 0%, var(--sky-bottom) 52%, var(--machine) 70%, var(--earth) 100%);
  }
  .experience { position: absolute; left: 0; right: 0; top: 18px; text-align: center; color: #fff; }
  .experience .lead { font-size: 34px; font-weight: 600; line-height: 1.2; }
  .experience .number { font-family: "Montserrat", sans-serif; font-weight: 800; font-size: 140px; line-height: 1; margin-top: -2px; }
  .experience .tail { font-size: 30px; font-weight: 600; line-height: 1.2; margin-top: -4px; }
</style>
</head>
<body>
  <section class="page cover">
    <div class="brand">
      <span class="brand-square"></span>
      <span class="brand-name">VELTA</span>
    </div>
    <div class="header-rule"></div>
    <div class="cover-photo" role="img" aria-label="Excavator loading a dump truck on a sandy site by the sea"></div>
    <div class="focus-frame"></div>
    <h1 class="cover-title">
      <div class="line-1">شاحنات</div>
      <div class="line-2">قطع الغيار</div>
    </h1>
    <p class="cover-sub">قطع غيار أصلية<br>صيانة وتدخل سريع</p>
    <p class="cover-url">www.veltaparts.example</p>
  </section>

  <section class="page back">
    <div class="back-photo" role="img" aria-label="Yellow excavator and dump truck on an earth mound under a blue sky"></div>
    <div class="experience">
      <div class="lead">من أكثر</div>
      <div class="number">60</div>
      <div class="tail">عام خبرة</div>
    </div>
  </section>
</body>
</html>
```